Business Card Design

I am after a business card design to be made for my pet care business in Darwin, Northern Territory Australia called Merrily Mutts. I am a certified canine trainer and offer training classes from puppy love class, basic obedience classes, intermediate classes, private lessons, mobile dog wash and grooming and pet minding. I currently have a logo that I would like used on the card that incorporates different shades of orange with the writing in black. I really want my card to stand out from the rest and look professional, easy to read with 'the edge' factor. Im thinking both sides printed on with contact details on one side and services provided on the back
Updates

Thank you all so much for your time. I am overwhelmed with designs as they are all 

really great. My business partner and myself have shortlisted a few that really caught our eye and
Will update as soon as we decide. 

Once again thank you to you all for your great designs :)

Industry/Entity Type

Training

Contact Information for Business Card

Merrily Mutts
merrilymutts@postlark.example
merrilymutts.example.au
0437260000
pet minding
Puppy classes
basic obedience classes
intermediate obedience classes
private lessons
mobile dog wash and grooming
certified dog trainer
CDTQ certified
Police checked
fully insured
honest
reliable
find us on socialnook www.socialnook.example/merrilymutts

Requirements
Must have
• My current logo either the stacked version or side by side - whatever works best and must include my services

```html
<!DOCTYPE html>
<html lang="en">
<head>
<meta charset="utf-8">
<title>Merrily Mutts – Business Card</title>
<link rel="stylesheet" href="https://fonts.googleapis.com/css2?family=Questrial&family=Josefin+Sans:wght@400&family=Dancing+Script:wght@500&display=swap">
<style>
  :root {
    --ink: #111111;
    --paper: #ffffff;
    --gold: #c9a227;
    --gold-deep: #b8901e;
    --gold-light: #efe3b5;
  }
  html, body {
    margin: 0;
    padding: 0;
    overflow: hidden;
    background: var(--paper);
  }
  .card {
    position: relative;
    width: 972px;
    height: 1200px;
    background: var(--paper);
    color: var(--ink);
    overflow: hidden;
    font-family: "Questrial", sans-serif;
  }
  .brand-mark {
    position: absolute;
    left: 92px;
    top: 98px;
    width: 226px;
    height: 226px;
  }
  .brand-rule {
    position: absolute;
    left: 354px;
    top: 74px;
    width: 2px;
    height: 272px;
    background: var(--ink);
  }
  .brand-name {
    position: absolute;
    left: 416px;
    top: 118px;
    margin: 0;
    font-family: "Questrial", sans-serif;
    font-weight: 400;
    font-size: 84px;
    line-height: 102px;
    letter-spacing: 3px;
    white-space: nowrap;
  }
  .tagline {
    position: absolute;
    left: 370px;
    width: 500px;
    top: 348px;
    margin: 0;
    text-align: center;
    font-family: "Dancing Script", cursive;
    font-weight: 500;
    font-size: 38px;
    white-space: nowrap;
  }
  .contact {
    position: absolute;
    top: 442px;
    left: 0;
    width: 972px;
    height: 70px;
  }
  .contact__email {
    position: absolute;
    right: 510px;
    top: 20px;
    font-size: 23px;
    white-space: nowrap;
  }
  .contact__divider {
    position: absolute;
    left: 481px;
    top: 0;
    width: 2px;
    height: 70px;
    background: var(--ink);
  }
  .contact__web {
    position: absolute;
    left: 506px;
    top: 20px;
    font-size: 23px;
    white-space: nowrap;
  }
  .contact__phone {
    position: absolute;
    top: 528px;
    left: 0;
    width: 972px;
    text-align: center;
    font-family: "Josefin Sans", sans-serif;
    font-size: 38px;
    letter-spacing: 0.5px;
  }
  .card-fold {
    position: absolute;
    left: 0;
    top: 640px;
    width: 972px;
    height: 2px;
    background: var(--ink);
  }
  .services {
    position: absolute;
    top: 682px;
    left: 0;
    width: 972px;
    margin: 0;
    padding: 0;
    list-style: none;
    text-align: center;
    font-family: "Josefin Sans", sans-serif;
    font-size: 41px;
    line-height: 61.4px;
  }
  .services__line {
    white-space: nowrap;
  }
  .services__sep {
    display: inline-block;
    width: 3px;
    height: 0.9em;
    margin: 0 0.28em;
    vertical-align: -0.05em;
    background: var(--gold);
  }
</style>
</head>
<body>
  <main class="card">
    <section class="card-front">
      <div class="brand-mark" role="img" aria-label="Merrily Mutts brand mark">
        <svg width="226" height="226" viewBox="0 0 226 226">
          <defs>
            <radialGradient id="markTone" cx="40%" cy="35%" r="70%">
              <stop offset="0%" stop-color="var(--gold-light)"/>
              <stop offset="100%" stop-color="var(--gold)"/>
            </radialGradient>
          </defs>
          <circle cx="113" cy="113" r="110" fill="url(#markTone)"/>
        </svg>
      </div>
      <div class="brand-rule"></div>
      <h1 class="brand-name">MERRILY<br>MUTTS</h1>
      <p class="tagline">“It’s awesome, to be merry”</p>
      <div class="contact">
        <span class="contact__email">merrilymutts@postlark.example</span>
        <span class="contact__divider"></span>
        <span class="contact__web">merrilymutts.example.au</span>
      </div>
      <div class="contact__phone">043-726-0000</div>
    </section>

    <div class="card-fold"></div>

    <ul class="services">
      <li class="services__line">Pet minding<span class="services__sep"></span>Puppy classes<span class="services__sep"></span>Basic obedience</li>
      <li class="services__line">classes<span class="services__sep"></span>Intermediate obedience classes</li>
      <li class="services__line">Private lessons<span class="services__sep"></span>Mobile dog wash and</li>
      <li class="services__line">grooming<span class="services__sep"></span>Certified dog trainer</li>
      <li class="services__line">CDTQ certified<span class="services__sep"></span>Police checked<span class="services__sep"></span>Fully insured</li>
      <li class="services__line">Honest<span class="services__sep"></span>Reliable</li>
      <li class="services__line">Find us on socialnook</li>
      <li class="services__line">www.socialnook.example/merrilymutts</li>
    </ul>
  </main>
</body>
</html>
```